LET ME HANDLE YOUR AUCTION NEEDS!

I am here to handle all your auction needs, I have over 20 years of auction experience buying and selling for dealerships in North Carolina and Tennessee. Send me to the sale to either rep your vehicles or let me know what you need and I can be
another set of eyes to help you buy what is hot and bad credit cars are my specialty. You know a car always sells better with a familiar face rather than auction personnel and with my great reputation I will be able to help find the buyers for your aged inventory.
Call me today and let's get started.
Rob Kellner 555-287-6390
(please have pictures of vehicles or an auto auction in the design)

```html
<!DOCTYPE html>
<html lang="en">
<head>
<meta charset="utf-8">
<title>Rob Kellner Auction Service</title>
<link rel="stylesheet" href="https://fonts.googleapis.com/css2?family=Tinos:ital,wght@0,400;0,700;1,400;1,700&family=Open+Sans:wght@700;800&display=swap">
<style>
  :root {
    --backdrop: #2b2b2d;
    --flyer-black: #050505;
    --brand-red: #c8080c;
    --accent-red: #e8141a;
    --paper-white: #ffffff;
    --ink: #111111;
  }
  * { margin: 0; padding: 0; box-sizing: border-box; }
  html, body {
    width: 1200px;
    height: 563px;
    overflow: hidden;
    background: var(--backdrop);
  }
  .flyer {
    position: absolute;
    left: 260px;
    top: 26px;
    width: 680px;
    height: 510px;
    background: var(--flyer-black);
    overflow: hidden;
    font-family: "Tinos", "Times New Roman", serif;
  }
  .title-band {
    position: absolute;
    left: 0; top: 0;
    width: 100%;
    height: 72px;
    background: var(--brand-red);
    display: flex;
    align-items: center;
    justify-content: center;
  }
  .title-band h1 {
    color: var(--paper-white);
    font-style: italic;
    font-weight: 700;
    font-size: 36px;
    letter-spacing: 2px;
  }
  .tagline-band {
    position: absolute;
    left: 0; top: 160px;
    width: 100%;
    height: 145px;
    background: var(--paper-white);
  }
  .vehicle-lineup {
    position: absolute;
    left: 70px;
    top: 92px;
    width: 560px;
    height: 130px;
    border-radius: 40px 40px 14px 14px;
    background:
      radial-gradient(ellipse at 88% 40%, #a8141c 0%, rgba(168,20,28,0) 22%),
      radial-gradient(ellipse at 6% 65%, #8e1a1e 0%, rgba(142,26,30,0) 16%),
      linear-gradient(180deg, #8a8e94 0%, #c4c8cc 35%, #4a4d52 70%, #1a1a1c 100%);
  }
  .tagline {
    position: absolute;
    left: 0;
    width: 470px;
    top: 232px;
    text-align: center;
    line-height: 1;
  }
  .tagline .lead {
    display: block;
    color: var(--ink);
    font-size: 25px;
  }
  .tagline .focus {
    display: block;
    color: var(--accent-red);
    font-weight: 700;
    font-size: 34px;
    margin-top: 4px;
    letter-spacing: 1px;
  }
  .experience-badge {
    position: absolute;
    left: 490px;
    top: 200px;
    width: 190px;
    height: 190px;
  }
  .experience-badge p {
    position: absolute;
    inset: 0;
    display: flex;
    align-items: center;
    justify-content: center;
    text-align: center;
    color: var(--paper-white);
    font-family: "Open Sans", Arial, sans-serif;
    font-weight: 800;
    font-size: 16px;
    line-height: 1.1;
  }
  .call-to-action {
    position: absolute;
    left: 40px;
    top: 318px;
    line-height: 1;
  }
  .call-to-action .kicker {
    display: block;
    color: var(--paper-white);
    font-style: italic;
    font-size: 40px;
    letter-spacing: 1px;
  }
  .call-to-action .urgent {
    display: block;
    color: var(--accent-red);
    font-weight: 700;
    font-size: 42px;
    margin-top: 6px;
    letter-spacing: 1px;
  }
  .contact {
    position: absolute;
    left: 40px;
    top: 430px;
    display: flex;
    align-items: center;
    gap: 18px;
  }
  .contact .name {
    color: var(--paper-white);
    font-weight: 700;
    font-size: 44px;
    letter-spacing: 1px;
  }
  .contact .phone {
    display: flex;
    align-items: center;
    gap: 8px;
    color: var(--accent-red);
    font-weight: 700;
    font-size: 46px;
  }
  .contact .phone svg { width: 40px; height: 40px; }
</style>
</head>
<body>
  <main class="flyer">
    <header class="title-band">
      <h1>ROB KELLNER AUCTION SERVICE</h1>
    </header>

    <div class="tagline-band"></div>

    <div class="vehicle-lineup" role="img" aria-label="Row of cars, trucks and SUVs lined up for auction"></div>

    <p class="tagline">
      <span class="lead">Let Me Handle All Of Your</span>
      <span class="focus">AUCTION NEEDS</span>
    </p>

    <div class="experience-badge">
      <svg viewBox="0 0 190 190" width="190" height="190" aria-hidden="true">
        <polygon fill="#e8141a" points="95,5 107,40 135,15 132,52 170,40 150,72 185,85 152,100 178,130 140,128 145,168 113,146 95,185 77,146 45,168 50,128 12,130 38,100 5,85 40,72 20,40 58,52 55,15 83,40"/>
      </svg>
      <p>OVER 20<br>YEARS<br>EXPERIENCE</p>
    </div>

    <p class="call-to-action">
      <span class="kicker">Let‘s Get Started</span>
      <span class="urgent">CALL NOW!</span>
    </p>

    <div class="contact">
      <span class="name">Rob Kellner</span>
      <span class="phone">
        <svg viewBox="0 0 40 40" aria-hidden="true">
          <circle cx="20" cy="20" r="17" fill="none" stroke="#e8141a" stroke-width="3"/>
          <path fill="#e8141a" d="M14 10c2 0 3 4 3 5s-2 2-2 3c1 3 3 5 6 7 1 0 2-2 3-2s5 1 5 3-2 4-4 4C17 30 10 22 10 14c0-2 2-4 4-4z"/>
        </svg>
        555-287-6390
      </span>
    </div>
  </main>
</body>
</html>
```